Whitcombe Framing Works - Card Design

I am looking to use the logo designs that you already did for me to develop a business card. I would like the card to have a black background and be double sided. I want white and green logo and text. I have attached an inspiration photo of a look that I like. I would like to use the Vertical Logo attached to take up the full front side of the card. On the back where I have my name and information, I would like to have the horizontal logo or maybe even just the image of the 'A' and trees without the text. I am open, but I am looking for something clean and simple and I want the green to really pop! Additional files can be found under Design #: 40593216

Target Market(s)

Homeowners

Industry/Entity Type

Construction

Contact Information for Business Card

Name: Marcus Pellow, Title: Project Manager, Phone: 831.555.0147, Email: whitcombeframingworks@mailbarn.net, address: 418 Juniper Ln, Felton, CA 95092, Lic# 2046318

Colors
00AB8E
00BBA5
67D7C9
C6EFE9
E9F9F6

Requirements
Nice to have
• I would like to see the logos that I have already got from SketchHarbor, though I am open to new ones

```html
<!DOCTYPE html>
<html lang="en">
<head>
<meta charset="utf-8">
<title>Whitcombe Framing Works – Business Card</title>
<link rel="stylesheet" href="https://fonts.googleapis.com/css2?family=Nunito+Sans:wght@400;700&display=swap">
<style>
  :root {
    --page-bg: #3b3b3c;
    --card-top: #2f2b2c;
    --card-bottom: #1f1c1d;
    --green: #6cc04a;
    --white: #f4f4f4;
    --silver: #a9a9ab;
  }
  * { box-sizing: border-box; margin: 0; padding: 0; }
  html, body {
    width: 1200px; height: 1200px; overflow: hidden;
    background: var(--page-bg);
    font-family: "Nunito Sans", Arial, sans-serif;
  }
  .sheet {
    width: 1200px; height: 1200px;
    display: flex; flex-direction: column; align-items: center; justify-content: center;
    gap: 60px;
  }
  .card {
    position: relative;
    width: 840px; height: 480px;
    background: radial-gradient(ellipse at 55% 40%, #3a3536 0%, var(--card-top) 40%, var(--card-bottom) 100%);
    box-shadow: 0 14px 30px rgba(0,0,0,.45);
  }
  /* front side */
  .card--front { display: flex; align-items: center; justify-content: center; }
  .front-mark {
    display: flex; align-items: center; gap: 18px;
    color: var(--silver); font-weight: 700; font-size: 40px; letter-spacing: .06em;
    text-transform: uppercase;
  }
  .mark-square { width: 34px; height: 34px; background: currentColor; }

  /* back side */
  .holder-name {
    position: absolute; left: 64px; top: 62px;
    color: var(--green); font-weight: 700; font-size: 38px; letter-spacing: .01em;
  }
  .holder-title {
    position: absolute; left: 64px; top: 112px;
    color: var(--white); font-size: 19px;
  }
  .address {
    position: absolute; left: 64px; top: 200px;
    color: var(--white); font-size: 19px; line-height: 1.35;
  }
  .contacts {
    position: absolute; left: 64px; top: 268px;
    list-style: none; color: var(--white); font-size: 19px;
  }
  .contacts li { display: flex; align-items: center; gap: 10px; margin-bottom: 8px; }
  .contacts svg { width: 16px; height: 16px; fill: var(--green); flex: none; }
  .back-mark {
    position: absolute; left: 470px; top: 196px;
    display: flex; align-items: center; gap: 12px;
    color: var(--white); font-weight: 700; font-size: 24px; letter-spacing: .04em;
    text-transform: uppercase;
  }
  .back-mark .mark-square { width: 24px; height: 24px; background: var(--green); }
  .license {
    position: absolute; left: 560px; top: 410px;
    color: var(--white); font-size: 20px;
  }
</style>
</head>
<body>
<main class="sheet">
  <section class="card card--front" aria-label="Card front">
    <div class="front-mark"><span class="mark-square"></span>Whitcombe Framing Works</div>
  </section>

  <section class="card card--back" aria-label="Card back">
    <h1 class="holder-name">Marcus Pellow</h1>
    <p class="holder-title">Project Manager</p>
    <p class="address">418 Juniper Ln, Felton,<br>CA 95092</p>
    <ul class="contacts">
      <li>
        <svg viewBox="0 0 16 16" aria-hidden="true"><path d="M3.6 1.2l2.2 2.6-1.3 1.7c.9 2 2.3 3.5 4.3 4.4l1.7-1.3 2.6 2.2-1.3 2.4C6.6 13 2.8 9.3 1.2 3.2z"/></svg>
        831.555.0147
      </li>
      <li>
        <svg viewBox="0 0 16 16" aria-hidden="true"><path d="M1 3h14v10H1z M1.6 3.6L8 8.6l6.4-5z" fill-rule="evenodd"/></svg>
        whitcombeframingworks@mailbarn.net
      </li>
    </ul>
    <div class="back-mark"><span class="mark-square"></span>Whitcombe Framing Works</div>
    <p class="license">Lic# 2046318</p>
  </section>
</main>
</body>
</html>
```